logo and label design for a vegan skincare Called Plantavive

We need a logo and label design for a skincare brand called plantavive based in Australia. The products are 100% natural, Australian made, small batch, vegan, cruelty-free, ethical and sustainable beauty products. The secret of our skin care products are their naturally active ingredients.
They are potent, yet incredibly gentle on sensitive skin. We believe in investing in only the highest quality and ethical ingredients to ensure we are creating products we can stand behind.
Our products use: Naturally delivered ingredients; Organic ingredients where is possible; Australian oils, fruits & Extracts; Aromatherapy oils; sustainable & ethical ingredients; natural preservatives.
Our products don't use: sulphates; parabens; phthalates; Petrochemicals; synthetic colours; synthetic fragrances. All label must be design for an amber bottle.
Label Requirements:
* 300 DPI minimum
* All fonts have been outlined
* 3mm Bleed included in artwork
Colors
Designer to choose colors to be used in the design.
Look and feel
Each slider illustrates characteristics of the customer's brand and the style your logo design should communicate.

```html
<!DOCTYPE html>
<html lang="en">
<head>
<meta charset="utf-8">
<title>Plantavive – Label, Logo and Product Board</title>
<link rel="stylesheet" href="https://fonts.googleapis.com/css2?family=Titillium+Web:wght@300;400&family=Oswald:wght@700&family=Josefin+Sans:wght@300&display=swap">
<style>
  :root {
    --ink: #111111;
    --board: #ffffff;
    --logo-panel: #e0e0e0;
    --leaf-mint: #d6ede0;
    --leaf-mint-deep: #bfe2cf;
    --rule: #6b6b6b;
    --scene-light: #f4f4f2;
    --scene-mid: #dcdcd8;
    --wood-light: #cdb89c;
    --wood-dark: #8c7457;
  }
  * { margin: 0; padding: 0; box-sizing: border-box; }
  html, body { width: 1200px; height: 1108px; overflow: hidden; background: var(--board); }
  .board { position: relative; width: 1200px; height: 1108px; font-family: "Titillium Web", sans-serif; color: var(--ink); }

  .section-title { position: absolute; font-family: "Titillium Web", sans-serif; font-weight: 300; font-size: 25px; letter-spacing: 0.5px; line-height: 1; z-index: 2; }
  .section-title--label { left: 26px; top: 38px; }
  .section-title--logo { left: 26px; top: 573px; }
  .section-title--product { left: 578px; top: 573px; }

  /* Label artwork */
  .label { position: absolute; left: 290px; top: 98px; width: 528px; height: 369px; overflow: hidden; }
  .label__pattern { position: absolute; inset: 0; background: linear-gradient(135deg, var(--leaf-mint) 0%, #e8f5ee 45%, var(--leaf-mint-deep) 100%); }
  .label__brand { position: absolute; left: 213px; top: 22px; width: 104px; height: 104px; border: 1px solid var(--ink); border-radius: 50%; background: #ffffff; display: flex; align-items: center; justify-content: center; }
  .label__brand-name { font-family: "Josefin Sans", sans-serif; font-weight: 300; font-size: 10px; letter-spacing: 2px; text-transform: uppercase; }
  .label__rule { position: absolute; left: 37px; top: 143px; width: 416px; height: 0; border-top: 0.6px solid var(--rule); }
  .label__title { position: absolute; left: 41px; top: 150px; font-family: "Oswald", sans-serif; font-weight: 700; font-size: 26px; letter-spacing: 3.4px; line-height: 1.2; }
  .label__copy { position: absolute; left: 40px; top: 196px; width: 410px; font-size: 8.3px; line-height: 10.5px; letter-spacing: -0.05px; }
  .label__copy p + p { margin-top: 10px; }
  .label__volume { position: absolute; left: 40px; top: 336px; font-size: 13.5px; line-height: 1; }

  /* Logo panel */
  .logo-panel { position: absolute; left: 0; top: 554px; width: 554px; height: 554px; background: var(--logo-panel); }
  .logo-panel__mark { position: absolute; left: 85px; top: 95px; width: 384px; height: 384px; border: 3px solid var(--ink); border-radius: 50%; background: #ffffff; display: flex; align-items: center; justify-content: center; }
  .logo-panel__name { font-family: "Josefin Sans", sans-serif; font-weight: 300; font-size: 30px; letter-spacing: 6px; text-transform: uppercase; }

  /* Product panel */
  .product-panel { position: absolute; left: 554px; top: 554px; width: 646px; height: 554px; }
  .product-panel__scene { position: absolute; inset: 0; background: linear-gradient(180deg, var(--scene-light) 0%, var(--scene-mid) 60%, var(--wood-light) 72%, var(--wood-dark) 100%); }
</style>
</head>
<body>
<main class="board">
  <h2 class="section-title section-title--label">Label</h2>

  <section class="label">
    <div class="label__pattern" role="img" aria-label="Pale mint line drawing of tropical palm and monstera leaves covering the label background"></div>
    <div class="label__brand"><span class="label__brand-name">Plantavive</span></div>
    <div class="label__rule"></div>
    <h1 class="label__title">Purifying Gel Cleanser</h1>
    <div class="label__copy">
      <p>Directions: Gently massage in circular motions onto damp skin, avoiding eye area. Rinse away with warm water or face cloth. Follow with your favourite moisturiser. Use morning and night.</p>
      <p>Ingredients: Purified Water, Lauryl Glucoside (Coconut &amp; Sugar Derived), Glycerin*, Cocamido Propyl Betaine (Coconut Derived), Triticum Aestivum Leaf Extract (Wheatgrass), Camellia Sinensis Leaf Extract (Green Tea), Chlorophyll (Alfalfa Grass), Citrus Sinensis (Orange) Oil, Carum Petroselinum Herb Extract (Parsley Seed), Myroxylon Pereirae (Peru Balsam) Oil, Leptospermum Petersonii (Lemon Tea Tree) Oil, Citrus Aurantium Var Amara (Petitgrain) Oil, Tocopherol (Vitamin E), Citric Acid, Hydroxymethylglycinate (Glycine Derived) - * Organic Ingredients</p>
      <p>Store in a cool dry place<br>Caution For external use only. Avoid contact with eyes. If irritation occurs, discontinue use.</p>
    </div>
    <div class="label__volume">200ml ℮</div>
  </section>

  <section class="logo-panel">
    <div class="logo-panel__mark"><span class="logo-panel__name">Plantavive</span></div>
  </section>
  <h2 class="section-title section-title--logo">Logo</h2>

  <section class="product-panel">
    <div class="product-panel__scene" role="img" aria-label="Photograph of a white pump bottle wearing the Purifying Gel Cleanser label, standing on a wooden table in a bright room"></div>
  </section>
  <h2 class="section-title section-title--product">Product</h2>
</main>
</body>
</html>
```